Veltro Coaching Business Card

We need a business card designed for a a company called "Veltro Coaching". We offer consulting, coaching and training to business leaders and coaches (across the world) using the latest findings in neuroscience, social and emotional intelligence and positive psychology. The final design should communicate the use of brain science to create sustainable relationships.

The card should be doublesided. The logo is attached and names and titles will be provided to the successful designer. Thank you.

Industry/Entity Type

Training

```html
<!DOCTYPE html>
<html lang="en">
<head>
<meta charset="utf-8">
<title>Veltro Coaching Business Card</title>
<link rel="stylesheet" href="https://fonts.googleapis.com/css2?family=Anton&family=Archivo+Black&family=Ubuntu:wght@400;500&display=swap">
<style>
  :root {
    --bg-light: #d9d9d9;
    --bg-dark: #8a8a8a;
    --card-white: #ffffff;
    --card-black: #0b0b0b;
    --card-black-soft: #1c1c1c;
    --lime: #a6ce39;
    --lime-bright: #d8ef3a;
    --brand-blue: #1a8ac6;
    --ink: #111111;
    --text-light: #f2f2f2;
  }
  * { margin: 0; padding: 0; box-sizing: border-box; }
  html, body { width: 1200px; height: 900px; overflow: hidden; }
  body {
    background: radial-gradient(ellipse at 50% 40%, var(--bg-light) 0%, var(--bg-dark) 100%);
    font-family: "Ubuntu", sans-serif;
    position: relative;
  }
  .card {
    position: absolute;
    width: 640px;
    height: 366px;
    background: var(--card-black);
    overflow: hidden;
    box-shadow: 0 10px 28px rgba(0,0,0,0.35);
  }
  .card--front { left: 100px; top: 70px; }
  .card--back  { left: 460px; top: 480px; }

  .card__top {
    position: absolute; left: 0; top: 0; width: 100%; height: 146px;
    background: var(--card-white);
  }
  .card__rule {
    position: absolute; left: 0; top: 146px; width: 100%; height: 7px;
    background: var(--lime);
  }
  .card--back .card__rule {
    background: linear-gradient(90deg, var(--lime) 0%, var(--lime) 60%, var(--lime-bright) 100%);
  }
  .card__bottom {
    position: absolute; left: 0; top: 153px; width: 100%; bottom: 0;
    background: linear-gradient(160deg, var(--card-black) 0%, var(--card-black) 55%, var(--card-black-soft) 100%);
  }

  .brand {
    position: absolute; left: 44px; top: 22px; width: 150px;
    display: flex; flex-direction: column; align-items: center; gap: 8px;
  }
  .brand__dot {
    width: 62px; height: 62px; border-radius: 50%;
    background: var(--brand-blue);
  }
  .brand__name {
    font-family: "Ubuntu", sans-serif; font-weight: 500;
    font-size: 17px; letter-spacing: 0.5px; color: var(--brand-blue);
    text-transform: uppercase; white-space: nowrap;
  }

  .title {
    position: absolute; left: 228px; top: 38px;
    font-family: "Anton", sans-serif; font-size: 54px; line-height: 1;
    color: var(--lime); letter-spacing: 1px; white-space: nowrap;
  }
  .motto {
    position: absolute; left: 70px; top: 205px;
    color: var(--text-light); font-size: 19px; letter-spacing: 0.6px;
  }

  .person { position: absolute; right: 44px; top: 48px; text-align: left; }
  .person__name {
    font-family: "Archivo Black", sans-serif; font-size: 40px; line-height: 1;
    color: var(--ink); letter-spacing: 1px;
  }
  .person__role {
    font-family: "Archivo Black", sans-serif; font-size: 15px;
    color: var(--ink); letter-spacing: 1px; margin-top: 6px;
  }

  .contacts {
    position: absolute; left: 30px; right: 20px; top: 190px;
    display: flex; align-items: flex-start;
  }
  .contact { padding: 0 22px; }
  .contact + .contact { border-left: 2px solid var(--lime); }
  .contact:first-child { padding-left: 0; }
  .contact__label { color: var(--lime); font-size: 16px; margin-bottom: 6px; }
  .contact__line { color: var(--text-light); font-size: 16px; line-height: 1.25; white-space: nowrap; }
</style>
</head>
<body>

  <section class="card card--front" aria-label="Business card front">
    <div class="card__top"></div>
    <div class="card__rule"></div>
    <div class="card__bottom"></div>
    <div class="brand">
      <span class="brand__dot"></span>
      <span class="brand__name">Veltro Coaching</span>
    </div>
    <h1 class="title">VELTRO COACHING</h1>
    <p class="motto">What does your company do or tags or a motto</p>
  </section>

  <section class="card card--back" aria-label="Business card back">
    <div class="card__top"></div>
    <div class="card__rule"></div>
    <div class="card__bottom"></div>
    <div class="brand">
      <span class="brand__dot"></span>
      <span class="brand__name">Veltro Coaching</span>
    </div>
    <div class="person">
      <h2 class="person__name">MARA ELLISON</h2>
      <p class="person__role">PROFESSION</p>
    </div>
    <div class="contacts">
      <div class="contact">
        <p class="contact__label">Web:</p>
        <p class="contact__line">http://veltrocoaching.com</p>
        <p class="contact__line">hello@veltrocoaching.com</p>
      </div>
      <div class="contact">
        <p class="contact__label">Phone/Fax:</p>
        <p class="contact__line">555 014 220</p>
        <p class="contact__line">555 014 221</p>
      </div>
      <div class="contact">
        <p class="contact__label">Address:</p>
        <p class="contact__line">Address Line One</p>
        <p class="contact__line">Address Line Two</p>
      </div>
    </div>
  </section>

</body>
</html>
```